Kelvor Plant Services

We are a heavy diesel mechanical business with additional air con certificates, remapping engine rebuilt

Contact Information for Business Card

Company Name, Director Name, Managing Director, Contact details, email and website

Font styles to use
Serif
Script

```html
<!DOCTYPE html>
<html lang="en">
<head>
<meta charset="utf-8">
<title>Kelvor Plant Services – Business Card</title>
<link rel="stylesheet" href="https://fonts.googleapis.com/css2?family=Lato:wght@400;700&family=Poppins:wght@400;700&display=swap">
<style>
  :root {
    --navy: #050a63;
    --paper: #ececec;
    --ink: #111111;
    --white: #ffffff;
    --backdrop: #2b2b2b;
  }
  html, body {
    margin: 0;
    width: 1200px;
    height: 1200px;
    overflow: hidden;
    background: var(--backdrop);
  }
  .canvas { position: relative; width: 1200px; height: 1200px; }
  .card {
    position: absolute;
    left: 201px;
    width: 797px;
    height: 454px;
    overflow: hidden;
    box-shadow: 0 14px 30px rgba(0,0,0,0.55);
  }
  .card--front { top: 96px; background: var(--navy); }
  .card--back  { top: 656px; background: var(--navy); }
  .front-shape { position: absolute; inset: 0; }
  .identity {
    position: absolute;
    right: 44px;
    top: 42px;
    text-align: right;
    color: var(--white);
    font-family: "Lato", sans-serif;
  }
  .identity__name { font-size: 38px; font-weight: 700; letter-spacing: 1px; margin: 0; line-height: 1.1; }
  .identity__role { font-size: 22px; font-weight: 400; margin: 4px 0 0; letter-spacing: 0.5px; }
  .brand {
    position: absolute;
    display: flex;
    align-items: center;
    gap: 12px;
    font-family: "Poppins", sans-serif;
    font-weight: 700;
  }
  .brand__dot { border-radius: 50%; flex: none; }
  .brand__name { line-height: 1.05; }
  .card--front .brand { left: 50px; top: 86px; color: var(--navy); }
  .card--front .brand__dot { width: 30px; height: 30px; background: var(--ink); }
  .card--front .brand__name { font-size: 36px; width: 260px; }
  .card--back .brand { left: 0; right: 0; top: 0; bottom: 0; justify-content: center; color: var(--white); gap: 20px; }
  .card--back .brand__dot { width: 46px; height: 46px; background: var(--white); }
  .card--back .brand__name { font-size: 52px; }
  .contacts {
    position: absolute;
    left: 48px;
    top: 266px;
    margin: 0;
    padding: 0;
    list-style: none;
    font-family: "Poppins", sans-serif;
    color: var(--ink);
    font-size: 18px;
    letter-spacing: 0.3px;
  }
  .contacts li { display: flex; align-items: flex-start; gap: 14px; margin-bottom: 6px; line-height: 1.5; }
  .contacts li.phone { font-size: 22px; line-height: 1.3; }
  .contacts svg { width: 18px; height: 18px; flex: none; margin-top: 5px; fill: var(--navy); }
</style>
</head>
<body>
<div class="canvas">

  <section class="card card--front">
    <svg class="front-shape" viewBox="0 0 797 454" width="797" height="454" aria-hidden="true">
      <polygon points="0,0 256,0 596,218 532,454 0,454" fill="var(--ink)"/>
      <polygon points="0,0 246,0 584,220 520,454 0,454" fill="var(--paper)"/>
      <line x1="256" y1="0" x2="596" y2="218" stroke="var(--paper)" stroke-width="2"/>
    </svg>

    <div class="identity">
      <p class="identity__name">DANIEL HARROW</p>
      <p class="identity__role">Managing Director</p>
    </div>

    <div class="brand">
      <span class="brand__dot"></span>
      <span class="brand__name">Kelvor Plant Services</span>
    </div>

    <ul class="contacts">
      <li>
        <svg viewBox="0 0 24 24"><path d="M12 2a7 7 0 0 0-7 7c0 5 7 13 7 13s7-8 7-13a7 7 0 0 0-7-7zm0 9.5A2.5 2.5 0 1 1 12 6.5a2.5 2.5 0 0 1 0 5z"/></svg>
        <span>58 Foundry Lane, Unit 4B<br>Ashbridge, North Yorks, YO17 4RT</span>
      </li>
      <li class="phone">
        <svg viewBox="0 0 24 24"><path d="M6.6 10.8a15 15 0 0 0 6.6 6.6l2.2-2.2a1 1 0 0 1 1-.25 11.4 11.4 0 0 0 3.6.57 1 1 0 0 1 1 1V20a1 1 0 0 1-1 1A17 17 0 0 1 3 4a1 1 0 0 1 1-1h3.5a1 1 0 0 1 1 1c0 1.25.2 2.450.57 3.57a1 1 0 0 1-.25 1z"/></svg>
        <span>(354) 617-2093</span>
      </li>
      <li>
        <svg viewBox="0 0 24 24"><path d="M2 5h20v14H2zm2 2v.5l8 5 8-5V7zm0 3v7h16v-7l-8 5z"/></svg>
        <span>info@kelvorplantservices.com</span>
      </li>
      <li>
        <svg viewBox="0 0 24 24"><path d="M12 2a10 10 0 1 0 0 20 10 10 0 0 0 0-20zm0 2c1 0 2.3 2 2.8 5H9.2C9.7 6 11 4 12 4zM4.3 11h3.8a15 15 0 0 0 0 2H4.3a8 8 0 0 1 0-2zm1 4h3.1c.4 1.6 1 3 1.7 4A8 8 0 0 1 5.3 15zm0-6A8 8 0 0 1 10 5c-.7 1-1.3 2.4-1.700 4zM12 20c-1 0-2.3-2-2.8-5h5.6c-.5 3-1.8 5-2.8 5zm3.9-9h3.8a8 8 0 0 1 0 2h-3.8a15 15 0 0 0 0-2zm-2 8c.7-1 1.3-2.4 1.7-4h3.1a8 8 0 0 1-4.8 4zm1.7-10C15.2 7.4 14.6 6 13.9 5a8 8 0 0 1 4.8 4z"/></svg>
        <span>kelvorplantservices.com</span>
      </li>
    </ul>
  </section>

  <section class="card card--back">
    <div class="brand">
      <span class="brand__dot"></span>
      <span class="brand__name">Kelvor Plant Services</span>
    </div>
  </section>

</div>
</body>
</html>
```